Professional & Modern Technology Business Card

We need a business card for our software/technology firm. Our services include Program/Project Management, Project Controls and Enterprise Analytics. Our clients are usually in the Aviation, Public Works, Transportation and Electric & Water Utility industries. We serve both public and private clients. Would like a very professional, conservative but somewhat modern design. Design, Develop, Deploy is the corporate tagline. We have two offices. The headquarters is in Atlanta, GA and a satellite office In Savannah, GA. Corporate Logo Attached.
Looking to do website and corporate brochure after the successful completion of this project. Would like to begin a working relationship with best designers.
Tagline: Design, Develop, Deploy
Website: www.quelvanesystems.example
My Name: Marla Dunstead
My Title: CEO
Email: mdunstead@quelvanesystems.example
Atlanta Address:
87 Corliss Avenue, #2291
Atlanta, GA 30301
Office: 404.555.0182
Fax: 404.555.0147
Mobile: 404.555.0163
Savannah Address:
350 West Harrow Bend Road
Suite 720
Savannah, GA 31401
Office: 912.555.0139
Fax: 404.555.0147
Mobile: 404.555.0163
Updates
Please include the email address in your designs: mdunstead@quelvanesystems.example.
I appreciate everyone's design efforts. Just a few notes:
1. Please remove the mobile number from the cards
2. The backs of the cards can be utilized for writing notes. Make sure your design on the back of the card is conducive to clearly adding writing if needed.
3. No black backgrounds please
4. Only use the corporate logo on the front of the card. You can use portions of the logo design, but not the logo in totality.
Thank You
Industry/Entity Type
Conservative
Look and feel
Each slider illustrates characteristics of the customer's brand and the style your logo design should communicate.

```html
<!DOCTYPE html>
<html lang="en">
<head>
<meta charset="utf-8">
<title>Quelvane Systems, Inc. — Business Card</title>
<link rel="stylesheet" href="https://fonts.googleapis.com/css2?family=Barlow:wght@400;500;600&family=Barlow+Semi+Condensed:wght@600&display=swap">
<style>
  :root {
    --canvas: #e4e2de;
    --card-front: #3b4249;
    --card-light: #ededec;
    --ink: #2b2b2b;
    --ink-soft: #4a4a4a;
    --white: #ffffff;
    --brand-blue: #1f7fc4;
    --brand-green: #8dbb2c;
    --brand-yellow: #e1bf1a;
    --rule-green: #9cc23a;
  }
  * { box-sizing: border-box; margin: 0; padding: 0; }
  html, body {
    width: 1200px; height: 900px; overflow: hidden;
    background: var(--canvas);
    font-family: "Barlow", "Helvetica Neue", Arial, sans-serif;
  }
  .stage { position: relative; width: 1200px; height: 900px; }
  .card {
    position: absolute;
    width: 560px; height: 320px;
    box-shadow: 0 10px 24px rgba(0,0,0,.18);
  }
  .card--front { left: 120px; top: 100px; background: var(--card-front); }
  .card--back  { left: 520px; top: 480px; background: var(--card-light); color: var(--ink); }

  /* brand name lockup */
  .brand {
    position: absolute;
    display: flex; align-items: center; gap: 10px;
    font-family: "Barlow Semi Condensed", "Arial Narrow", sans-serif;
    font-weight: 600; letter-spacing: -0.01em; line-height: 1;
    white-space: nowrap;
  }
  .brand__dot { border-radius: 50%; flex: none; }
  .card--front .brand { left: 70px; top: 104px; font-size: 40px; color: var(--white); }
  .card--front .brand__dot { width: 30px; height: 30px; background: var(--brand-yellow); }
  .card--back .brand { left: 34px; top: 112px; font-size: 22px; color: var(--ink); }
  .card--back .brand__dot { width: 20px; height: 20px; background: var(--brand-yellow); }

  .front-rule {
    position: absolute; left: 300px; right: 0; top: 172px;
    height: 1px; background: var(--rule-green);
  }
  .tagline {
    position: absolute; left: 302px; top: 184px;
    font-size: 13px; font-weight: 600; letter-spacing: .08em;
    color: var(--white);
  }
  .tagline .t-blue { color: var(--brand-blue); }
  .tagline .t-green { color: var(--brand-green); }
  .tagline .t-yellow { color: var(--brand-yellow); }

  /* back card */
  .person { position: absolute; left: 300px; top: 38px; }
  .person__name {
    font-size: 20px; font-weight: 500; letter-spacing: .02em; text-transform: uppercase;
    white-space: nowrap;
  }
  .person__title { font-size: 16px; font-weight: 400; }
  .person__email { margin-top: 4px; font-size: 12px; color: var(--ink-soft); }
  .person__rule { margin-top: 8px; width: 240px; height: 1px; background: var(--rule-green); }

  .office { position: absolute; font-size: 13.5px; line-height: 1.32; color: var(--ink); font-style: normal; }
  .office--atl { left: 34px; top: 190px; }
  .office--sav { left: 300px; top: 130px; }
  .office .label { color: var(--brand-blue); font-weight: 600; }
  .office .web { color: var(--brand-blue); font-weight: 600; }
</style>
</head>
<body>
<main class="stage">

  <section class="card card--front" aria-label="Business card front">
    <div class="brand">
      <span class="brand__dot"></span>
      <span class="brand__name">Quelvane Systems, Inc.</span>
    </div>
    <div class="front-rule"></div>
    <p class="tagline">
      <span class="t-blue">DESIGN</span> . <span class="t-green">DEVELOP</span> . <span class="t-yellow">DEPLOY</span>
    </p>
  </section>

  <section class="card card--back" aria-label="Business card back">
    <div class="person">
      <p class="person__name">Marla Dunstead <span class="person__title">| CEO</span></p>
      <p class="person__email">mdunstead@quelvanesystems.example</p>
      <div class="person__rule"></div>
    </div>

    <div class="brand">
      <span class="brand__dot"></span>
      <span class="brand__name">Quelvane Systems, Inc.</span>
    </div>

    <address class="office office--sav">
      350 West Harrow Bend Road<br>
      Suite 720<br>
      Savannah, GA 31401<br>
      <span class="label">Office:</span> 912.555.0139<br>
      <span class="label">Fax:</span> 404.555.0147
    </address>

    <address class="office office--atl">
      87 Corliss Avenue, #2291<br>
      Atlanta, GA 30301<br>
      <span class="label">Office:</span> 404.555.0182<br>
      <span class="label">Fax:</span> 404.555.0147<br>
      <span class="web">www.quelvanesystems.example</span>
    </address>
  </section>

</main>
</body>
</html>
```